Business Card Design Project

Bold, modern, clean business card design needed. Prefer double sided with art logo on the back. Front of card with company name logo, no art.

Target Market(s)

Our consulting company supports local, state and federal law enforcement officers. Therefore the design should be clean and direct with no flash or arrogance to it.

Industry/Entity Type

Business

```html
<!DOCTYPE html>
<html lang="en">
<head>
<meta charset="utf-8">
<title>Castell Systems – Business Cards</title>
<link rel="stylesheet" href="https://fonts.googleapis.com/css2?family=Open+Sans:wght@400;600;700&display=swap">
<style>
  :root {
    --page-bg: #ece9e4;
    --card-black: #0d0f11;
    --card-black-top: #1c1f22;
    --card-white: #ffffff;
    --brand-green: #8cc63f;
    --brand-green-deep: #6aa81c;
    --ink: #1a1a1a;
    --ink-soft: #3a3a3a;
  }
  * { box-sizing: border-box; margin: 0; padding: 0; }
  html, body {
    width: 1200px;
    height: 913px;
    overflow: hidden;
  }
  body {
    background: var(--page-bg);
    font-family: "Open Sans", Arial, sans-serif;
    position: relative;
  }
  .card {
    position: absolute;
    width: 540px;
    height: 309px;
    border-radius: 4px;
    overflow: hidden;
    box-shadow: 0 10px 28px rgba(0,0,0,0.22);
  }
  /* Back side */
  .card-back {
    left: 40px;
    top: 302px;
    background: linear-gradient(160deg, var(--card-black-top), var(--card-black) 60%);
    display: flex;
    align-items: center;
    justify-content: center;
  }
  .brand {
    display: flex;
    align-items: center;
    gap: 12px;
  }
  .brand-mark {
    width: 22px;
    height: 22px;
    background: var(--brand-green);
  }
  .brand-name {
    font-weight: 700;
    font-size: 30px;
    letter-spacing: 3px;
  }
  .card-back .brand-name { color: #ffffff; }

  /* Front side */
  .card-front {
    left: 620px;
    top: 302px;
    background: var(--card-white);
  }
  .front-swoosh {
    position: absolute;
    inset: 0;
    width: 100%;
    height: 100%;
  }
  .card-front .brand {
    position: absolute;
    left: 36px;
    top: 168px;
  }
  .card-front .brand-name {
    color: var(--ink);
    font-size: 24px;
  }
  .contact-list {
    position: absolute;
    top: 14px;
    right: 20px;
    list-style: none;
    text-align: right;
    font-size: 11.5px;
    line-height: 17px;
    color: var(--ink-soft);
  }
  .contact-list li {
    display: flex;
    align-items: center;
    justify-content: flex-end;
    gap: 8px;
  }
  .contact-icon { width: 11px; height: 11px; flex: none; }
  .holder {
    position: absolute;
    right: 20px;
    top: 160px;
    text-align: right;
    color: #ffffff;
  }
  .holder-name { font-weight: 700; font-size: 15px; }
  .holder-role { font-size: 10.5px; margin-top: 1px; }
</style>
</head>
<body>

<section class="card card-back" aria-label="Card back">
  <div class="brand">
    <span class="brand-mark"></span>
    <span class="brand-name">CASTELL SYSTEMS</span>
  </div>
</section>

<section class="card card-front" aria-label="Card front">
  <svg class="front-swoosh" viewBox="0 0 540 309" preserveAspectRatio="none" aria-hidden="true">
    <defs>
      <linearGradient id="greenFill" x1="0" y1="0" x2="0.4" y2="1">
        <stop offset="0" stop-color="#a6d94f"/>
        <stop offset="1" stop-color="#6aa81c"/>
      </linearGradient>
    </defs>
    <path d="M0,300 C150,295 280,265 330,205 C365,160 385,115 425,104 C465,96 505,96 540,95 L540,309 L0,309 Z" fill="#1a1a1a"/>
    <path d="M0,305 C155,301 288,272 340,210 C372,165 392,122 432,111 C470,103 508,102 540,101 L540,309 L0,309 Z" fill="#ffffff"/>
    <path d="M100,309 C250,292 325,262 355,205 C385,150 405,118 445,112 C485,106 515,105 540,104 L540,309 Z" fill="url(#greenFill)"/>
  </svg>

  <div class="brand">
    <span class="brand-name">CASTELL SYSTEMS</span>
  </div>

  <ul class="contact-list">
    <li>Your Commercial or office address
      <svg class="contact-icon" viewBox="0 0 12 12"><path d="M6 0.5a4 4 0 0 1 4 4c0 3-4 7-4 7s-4-4-4-7a4 4 0 0 1 4-4z" fill="var(--brand-green)"/><circle cx="6" cy="4.5" r="1.5" fill="#fff"/></svg>
    </li>
    <li>00.00.00.0000 &nbsp;
      <svg class="contact-icon" viewBox="0 0 12 12"><rect x="1" y="2" width="10" height="8" rx="1.5" fill="var(--brand-green)"/><rect x="3" y="4" width="6" height="1.5" fill="#fff"/></svg>
      00.00.00.0000
      <svg class="contact-icon" viewBox="0 0 12 12"><path d="M2.5 1h2l1 3-1.5 1a6 6 0 0 0 3 3l1-1.5 3 1v2a1 1 0 0 1-1 1A9.5 9.5 0 0 1 1.5 2a1 1 0 0 1 1-1z" fill="var(--brand-green)"/></svg>
    </li>
    <li>yourname@yourwebsite.com
      <svg class="contact-icon" viewBox="0 0 12 12"><rect x="0.5" y="2.5" width="11" height="7.5" rx="1" fill="var(--brand-green)"/><path d="M1 3l5 4 5-4" stroke="#fff" stroke-width="1" fill="none"/></svg>
    </li>
    <li>www.yourwebsite.com
      <svg class="contact-icon" viewBox="0 0 12 12"><circle cx="6" cy="6" r="5.5" fill="var(--brand-green)"/><path d="M0.5 6h11M6 0.5c-3 3-3 8 0 11M6 0.5c3 3 3 8 0 11" stroke="#fff" stroke-width="0.8" fill="none"/></svg>
    </li>
  </ul>

  <div class="holder">
    <p class="holder-name">Your Long Name</p>
    <p class="holder-role">Managing Director</p>
  </div>
</section>

</body>
</html>
```